Store Front Signage for an Upscale Cake & Dessert Bakery

We need a design for store front windows. We are a 12 year old bakery specializing in cakes, cupcakes, cookies, pies, and other desserts. We recently moved to a high traffic location.. and we would like to boost our visual presence; we can be seen from the main road but are competing with other businesses for attention. Attached is a photo of our store front with posters but this signage will be for window film for the entire window span. (see the store front to the left of the photo to see the green and yellow as a film example)
Our logo and store sign (not like in photo, that is showing more red) are in shades of pink. The most visible part of the signage is in the upper third to upper half of the 60" panels.
The signs in the window currently say Life's Short. Eat Cake.
We now use Enjoy Life. Eat Cake.
The design should span all the windows and door -- this can be individual panels or one design that covers all panels. I have pink and greys chosen but please DO NOT let this constrain you. The inside of the bakery has grey floors and walls. white cabinetry, black granite countertops. The only thing with color is the baked goods and display cakes, pictures of cakes, the logo and menu and employee shirts.

Target Market(s)

we are located at a busy intersection --- we would like to capture the attention of people in cars as they pass by and entice them to stop in

Font styles to use
Serif
Sans Serif

Colors
d3d3d3
757575
ffffff
e24197
e667a6
eea4c8
f9d9e8

Requirements
Must have
• I would like the design to be easily discernible at the road way that is about 75 feet from store front. If you look at the photos I provide, note that the font size that is easily readable from the road are the ones in the top panes (although the shadow from the building makes them difficult to see -- the best visibility is the top 1/3 of the 60" panels.
Nice to have
• would like to have some non-photo graphics of a cake ( like a birthday cake), tiered cake, cupcakes, and cookies or pie for the panels --- but DO NOT let this constrain you. I need something to grab attention while cars are stopped at the nearby traffic light.
• If this design works well... I will be changing the panel on a seasonal basis
Should not have
• words that cannot be read from a distance.

```html
<!DOCTYPE html>
<html lang="en">
<head>
<meta charset="utf-8">
<title>Rosalind's Bake Shoppe – Window Film</title>
<link rel="stylesheet" href="https://fonts.googleapis.com/css2?family=Quicksand:wght@400;500;700&display=swap">
<style>
  :root {
    --canvas: #ecebea;
    --frame: #1b1b1d;
    --gold: #b08a3a;
    --white: #ffffff;
    --blush: #f6c9de;
    --pink: #e667a6;
    --hot-pink: #e24197;
    --plum: #9a2673;
    --plum-band: rgba(128, 26, 92, 0.9);
    --headline: #a0326f;
    --glass: #141416;
  }
  * { box-sizing: border-box; margin: 0; padding: 0; }
  html, body { width: 1200px; height: 636px; overflow: hidden; }
  body {
    background: var(--canvas);
    font-family: "Quicksand", "Helvetica Neue", Arial, sans-serif;
    position: relative;
  }
  .window-span {
    position: absolute;
    left: 84px; top: 33px;
    width: 1046px; height: 533px;
    background: var(--frame);
  }
  .pane { position: absolute; overflow: hidden; }

  /* upper category boards */
  .category {
    background: var(--gold);
    color: var(--white);
    display: flex; align-items: center; justify-content: center;
    text-align: center;
    font-size: 32px; font-weight: 400; line-height: 1.05;
    letter-spacing: 0.5px;
  }
  .transom { background: var(--glass); }

  /* middle illustrated panes */
  .artwork {
    position: absolute; inset: 0;
    background: linear-gradient(160deg, var(--hot-pink) 0%, var(--pink) 45%, var(--blush) 70%, #c98a3a 100%);
  }
  .artwork.swirl {
    background: linear-gradient(180deg, var(--blush) 0%, var(--pink) 45%, var(--hot-pink) 75%, #b57a3e 100%);
  }
  .slogan-field {
    position: absolute; left: 0; right: 0; top: 0; height: 111px;
    background: var(--blush);
    color: var(--headline);
    font-size: 43px; font-weight: 400; line-height: 1.05;
    text-align: center; padding-top: 4px;
  }
  .info-band {
    position: absolute; left: 0; right: 0; top: 111px; height: 41px;
    background: var(--plum-band);
    color: var(--white);
    font-size: 21px; font-weight: 500;
    display: flex; align-items: center; justify-content: center;
    white-space: nowrap;
  }

  /* lower kick panels */
  .kick { background: var(--plum); }

  /* entry door */
  .door { background: var(--white); }
  .door .brand {
    position: absolute; left: 0; right: 0; top: 0; height: 98px;
    display: flex; flex-direction: column; align-items: center; justify-content: center;
    color: var(--headline);
    font-size: 15px; font-weight: 700; line-height: 1.2; text-align: center;
  }
  .door .hours {
    position: absolute; left: 0; right: 0; top: 98px; height: 57px;
    background: var(--plum);
    color: var(--white);
    font-size: 9.5px; font-weight: 700; line-height: 1.3;
    text-align: center; padding-top: 7px;
  }
  .door .artwork { top: 155px; }
</style>
</head>
<body>
<main class="window-span" aria-label="Storefront window film">

  <!-- top row -->
  <div class="pane category" style="left:10px;top:10px;width:200px;height:147px;">custom<br>cakes</div>
  <div class="pane category" style="left:223px;top:10px;width:201px;height:147px;">holiday<br>desserts</div>
  <div class="pane transom" style="left:436px;top:10px;width:153px;height:147px;"></div>
  <div class="pane category" style="left:602px;top:10px;width:204px;height:147px;">cupcakes<br>cookies</div>
  <div class="pane category" style="left:823px;top:10px;width:213px;height:147px;">sweets<br>galore</div>

  <!-- middle row -->
  <section class="pane" style="left:10px;top:168px;width:200px;height:264px;">
    <div class="artwork" role="img" aria-label="Illustration of a layered cake slice with a cherry on top"></div>
    <div class="info-band">order online</div>
  </section>
  <section class="pane" style="left:223px;top:168px;width:201px;height:264px;">
    <div class="artwork swirl" role="img" aria-label="Illustration of a frosted cupcake with a cherry"></div>
    <div class="slogan-field">enjoy<br>life.</div>
    <div class="info-band">rosalindsbakes.com</div>
  </section>

  <section class="pane door" style="left:450px;top:181px;width:131px;height:317px;">
    <div class="brand">Rosalind's<br>Bake Shoppe</div>
    <div class="hours">HOURS:<br>MONDAY-SATURDAY<br>9AM - 7PM<br>SUNDAY 11AM-5PM</div>
    <div class="artwork swirl" role="img" aria-label="Illustration of a tall swirled pink cupcake"></div>
  </section>

  <section class="pane" style="left:602px;top:168px;width:204px;height:264px;">
    <div class="artwork" role="img" aria-label="Illustration of a heart-shaped cake with sprinkles"></div>
    <div class="slogan-field">eat<br>cake.</div>
    <div class="info-band">next day pick-up</div>
  </section>
  <section class="pane" style="left:823px;top:168px;width:213px;height:264px;">
    <div class="artwork swirl" role="img" aria-label="Illustration of a swirled cupcake topped with a strawberry"></div>
    <div class="info-band" style="top:111px;">delivery available</div>
  </section>

  <!-- bottom row -->
  <div class="pane kick" style="left:10px;top:437px;width:200px;height:86px;"></div>
  <div class="pane kick" style="left:223px;top:437px;width:201px;height:86px;"></div>
  <div class="pane kick" style="left:602px;top:437px;width:204px;height:86px;"></div>
  <div class="pane kick" style="left:823px;top:437px;width:213px;height:86px;"></div>

</main>
</body>
</html>
```